Three Ebook Covers for Short Stories

Three Ebook cover designs for 3 short stories (all linked) psychological thriller. I like clean crisp images. Perhaps with an imagine of eyes/part of face - white woman, 29, thin, brown eyes, short bob hair. I like gritty, moody, raw type of images. I dont mind the same image being used on three covers providing there are differences (ie slight variation in colour of book). Colours I prefer red, burgundy, black, grey, white. My website shows off the type of colours I prefer. www.lydiakbarnes-author.net
Branding is important.

Target Market(s)

Adult. Moth in Attic, Lost Field, type of readers.

Industry/Entity Type

Book Publisher

Font styles to use
Sans Serif
Other font styles liked:
• fonts used on thriller novels

Requirements
Must have
• Author Name: Lydia K Barnes
• Short Story as Part of Title
• Short Story 1: Title - First Crow
• Short Story 2: Title - Second Crow
• Short Story 3: Title - Third Crow
• Branding is important so they must look like they are a set.
• A font which is aligned to thriller type novels
• Colours aligned to my website - red, burgundy, white, grey, black.
Nice to have
• I don't mind a black and white type photo imagine.
Should not have
• n/a

```html
<!DOCTYPE html>
<html lang="en">
<head>
<meta charset="utf-8">
<title>Crow Trilogy – Ebook Covers</title>
<link rel="stylesheet" href="https://fonts.googleapis.com/css2?family=Cinzel:wght@400;600&display=swap">
<style>
  :root {
    --board: #d9d9d9;
    --ink: #000000;
    --skin: #a9a9a9;
    --skin-soft: #6e6e6e;
    --shadow: #2a2a2a;
    --silver-top: #f4f4f4;
    --silver-mid: #9a9a9a;
    --silver-low: #dcdcdc;
    --glow: #8c0a0a;
    --burgundy: #5a0a0e;
    --burgundy-deep: #2a0508;
    --red: #e00a0a;
    --author: #f0ecec;
    --rule: #8d8d8d;
  }
  * { box-sizing: border-box; margin: 0; padding: 0; }
  html, body { width: 1200px; height: 1200px; overflow: hidden; }
  body { background: var(--board); position: relative; font-family: "Cinzel", serif; }

  .cover { position: absolute; background: var(--ink); overflow: hidden; }
  .cover--first  { left: 150px; top: 6px;   width: 448px; height: 598px; }
  .cover--second { left: 608px; top: 6px;   width: 450px; height: 600px; }
  .cover--third  { left: 390px; top: 610px; width: 434px; height: 581px; }

  .cover__photo { position: absolute; top: 0; height: 100%; }
  .cover--first .cover__photo {
    left: 0; width: 370px;
    background:
      linear-gradient(90deg, rgba(0,0,0,0) 55%, rgba(0,0,0,0.85) 100%),
      radial-gradient(ellipse 60% 45% at 28% 30%, var(--skin) 0%, var(--skin-soft) 45%, rgba(0,0,0,0) 100%),
      radial-gradient(ellipse 40% 30% at 30% 80%, var(--skin-soft) 0%, rgba(0,0,0,0) 100%),
      linear-gradient(180deg, var(--shadow) 0%, #141414 100%);
  }
  .cover--second .cover__photo {
    right: 0; width: 300px;
    background:
      linear-gradient(270deg, rgba(0,0,0,0) 50%, rgba(0,0,0,0.9) 100%),
      radial-gradient(ellipse 55% 40% at 85% 28%, var(--skin) 0%, var(--skin-soft) 45%, rgba(0,0,0,0) 100%),
      radial-gradient(ellipse 35% 25% at 85% 85%, var(--skin-soft) 0%, rgba(0,0,0,0) 100%),
      linear-gradient(180deg, #1e1e1e 0%, #0c0c0c 100%);
  }
  .cover--third .cover__photo {
    left: 0; width: 220px;
    background:
      linear-gradient(90deg, rgba(0,0,0,0) 50%, rgba(0,0,0,0.85) 100%),
      radial-gradient(ellipse 45% 35% at 10% 30%, #585858 0%, #2a2a2a 55%, rgba(0,0,0,0) 100%),
      linear-gradient(180deg, #1c1c1c 0%, #0a0a0a 100%);
  }

  .cover__title {
    position: absolute;
    font-weight: 600;
    line-height: 0.86;
    letter-spacing: 1px;
    background: linear-gradient(180deg, var(--silver-top) 0%, var(--silver-mid) 55%, var(--silver-low) 100%);
    -webkit-background-clip: text; background-clip: text;
    color: transparent;
    filter: drop-shadow(0 0 3px var(--glow)) drop-shadow(0 0 2px var(--glow));
  }
  .cover__title-line { display: block; white-space: nowrap; }
  .cover__title-line--top { font-size: 60px; }
  .cover__title-line--bottom { font-size: 80px; }

  .cover--first .cover__title  { right: 24px; top: 306px; text-align: right; }
  .cover--second .cover__title { left: 20px;  top: 306px; text-align: left; }
  .cover--third .cover__title  { right: 26px; top: 296px; text-align: right; }

  .cover__tagline {
    position: absolute;
    font-size: 8px; letter-spacing: 0.5px;
    color: var(--author); text-transform: uppercase; white-space: nowrap;
  }
  .cover--first .cover__tagline  { right: 28px; top: 432px; }
  .cover--second .cover__tagline { left: 26px;  top: 434px; }
  .cover--third .cover__tagline  { left: 26px;  top: 418px; }

  .cover__band {
    position: absolute; left: 0; width: 100%; height: 94px;
  }
  .cover--first .cover__band {
    top: 456px;
    background: linear-gradient(90deg, var(--burgundy-deep) 0%, var(--burgundy) 30%, #3a0709 80%, rgba(20,0,0,0.6) 100%);
  }
  .cover--second .cover__band {
    top: 458px;
    background: linear-gradient(90deg, var(--red) 0%, #7a0608 20%, #3a0508 50%, rgba(60,8,10,0.4) 100%);
  }
  .cover--third .cover__band {
    top: 442px; height: 91px;
    background: linear-gradient(90deg, var(--burgundy) 0%, #4a080c 50%, rgba(40,4,6,0.5) 100%);
  }

  .cover__author {
    position: absolute; top: 50%; font-size: 19px; letter-spacing: 0.5px;
    color: var(--author); text-transform: uppercase; white-space: nowrap;
    transform: translate(-50%, -50%);
  }
  .cover--first .cover__author  { left: 224px; }
  .cover--second .cover__author { left: 224px; }
  .cover--third .cover__author  { left: 218px; }

  .cover__rule { position: absolute; height: 1px; background: var(--rule); }
  .cover--first .cover__rule  { left: 152px; right: 0; top: 555px; }
  .cover--second .cover__rule { left: 152px; right: 0; top: 557px; }
  .cover--third .cover__rule  { left: 146px; right: 0; top: 538px; }
</style>
</head>
<body>

<section class="cover cover--first">
  <div class="cover__photo" role="img" aria-label="Black and white photograph of a dark-eyed woman holding a finger to her lips"></div>
  <h1 class="cover__title"><span class="cover__title-line cover__title-line--top">First</span><span class="cover__title-line cover__title-line--bottom">Crow</span></h1>
  <p class="cover__tagline">A Psychological Thriller</p>
  <div class="cover__band"><p class="cover__author">Lydia K Barnes</p></div>
  <div class="cover__rule"></div>
</section>

<section class="cover cover--second">
  <div class="cover__photo" role="img" aria-label="Black and white photograph of a woman peering from the dark edge of the frame"></div>
  <h1 class="cover__title"><span class="cover__title-line cover__title-line--top">Second</span><span class="cover__title-line cover__title-line--bottom">Crow</span></h1>
  <p class="cover__tagline">A Psychological Thriller</p>
  <div class="cover__band"><p class="cover__author">Lydia K Barnes</p></div>
  <div class="cover__rule"></div>
</section>

<section class="cover cover--third">
  <div class="cover__photo" role="img" aria-label="Dark photograph of a woman half hidden behind long hair"></div>
  <h1 class="cover__title"><span class="cover__title-line cover__title-line--top">Third</span><span class="cover__title-line cover__title-line--bottom">Crow</span></h1>
  <p class="cover__tagline">A Psychological Thriller</p>
  <div class="cover__band"><p class="cover__author">Lydia K Barnes</p></div>
  <div class="cover__rule"></div>
</section>

</body>
</html>
```